Product Sales Website Design - E-commerce - Shopify etc

We have been selling printing equipment for some time now and think that it will be useful to sell the products on the internet, using a simple e-commerce platform, such as shopify etc. There are roughly a few dozen products - so basically, the idea is to have a modern, simple and clean home page. When someone looks at it, they think, this is it - I want to buy here. I am not going to impose any ideas or say how I want it done.

Just so you know, at the moment there are three categories of products. One being printers, scanners and accessories.

I am excited by this whole project and don't want to have good designers backing out because they feel i am imposing restrictions. Feel free to impress me.

Industry/Entity Type

E-Commerce

Requirements
Must have
• integration with an e-commerce platform is a must or show how to integrate, so I can easily introduce further products.

```html
<!DOCTYPE html>
<html lang="en">
<head>
<meta charset="utf-8">
<title>Inkwell Printing – Printers, Scanners &amp; Accessories</title>
<link href="https://fonts.googleapis.com/css2?family=Source+Sans+3:wght@400;600;700&family=Montserrat:wght@500;600&family=Arimo:wght@400;700&display=swap" rel="stylesheet">
<style>
:root{
  --blue:#0b64b0;
  --blue-dark:#08539a;
  --red:#cc0e0e;
  --green:#8bb23f;
  --ink:#222;
  --muted:#555;
  --line:#e2e2e2;
  --white:#fff;
  --black:#111;
}
*{box-sizing:border-box;margin:0;padding:0}
html,body{width:762px;height:1200px;overflow:hidden;background:var(--white)}
body{position:relative;font-family:"Source Sans 3",Arial,sans-serif;color:var(--ink)}
.abs{position:absolute}

/* header */
.brand{left:70px;top:14px;display:flex;align-items:center;gap:8px}
.brand-mark{width:26px;height:26px;border-radius:50%;background:var(--blue)}
.brand-name{font-size:19px;font-weight:600;color:var(--red)}
.call{left:376px;top:20px;display:flex;align-items:center;gap:8px;color:var(--red);font-size:13px}
.search{left:549px;top:19px;width:147px;height:18px;border:1px solid #d6d6d6;border-radius:2px;font-size:7px;color:#999;padding:4px 6px;display:flex;justify-content:space-between;align-items:center}

.nav{left:0;top:55px;width:762px;height:25px;background:var(--blue)}
.nav span{position:absolute;top:0;height:25px;line-height:25px;transform:translateX(-50%);color:var(--white);font-size:10.5px}
.nav .active{background:var(--red);width:70px;text-align:center}

/* intro */
.intro{left:0;top:93px;width:762px;text-align:center}
.intro h1{font-size:20px;font-weight:600;color:#222}
.intro p{font-size:9px;color:#333;margin-top:6px;font-family:Arimo,sans-serif}

/* showcase */
.showcase{left:74px;top:160px;width:614px;height:225px;border:1px solid var(--line);border-radius:4px}
.show-item{position:absolute;text-align:center;font-size:10px;color:#333}
.show-img{border-radius:6px}
.feature-card{left:272px;top:158px;width:213px;height:232px;background:var(--white);border:1px solid #ddd;border-radius:4px;box-shadow:0 0 8px rgba(0,0,0,.15);text-align:center}
.ribbon{position:absolute;left:0;top:0}
.ribbon-text{position:absolute;left:4px;top:5px;color:var(--white);text-align:left;line-height:1}
.ribbon-text b{font-size:12px;font-weight:600;display:block}
.ribbon-text small{font-size:7px;display:block;margin-top:1px}
.ribbon-text em{font-style:normal;font-size:11px;font-weight:700;display:block;margin-top:1px}
.feature-title{position:absolute;left:0;width:100%;top:163px;font-size:11px;color:var(--blue)}
.btn{display:inline-block;color:var(--white);border-radius:2px;text-align:center}
.btn-red{background:var(--red)}
.btn-blue{background:var(--blue)}
.feature-btns{position:absolute;left:0;width:100%;top:185px;display:flex;justify-content:center;gap:8px}
.feature-btns .btn{font-size:10px;height:18px;line-height:18px;width:70px}
.feature-btns .btn-blue{width:72px}
.stars{color:#111;letter-spacing:1px}
.feature-stars{position:absolute;left:0;width:100%;top:207px;font-size:10px}

/* offers */
.offer{top:424px;height:41px;border-radius:2px;color:var(--white);display:flex;align-items:center;padding-left:14px;gap:8px}
.offer-icon{width:24px;height:24px;border:2px solid var(--white);border-radius:50%;display:flex;align-items:center;justify-content:center}
.offer h3{font-family:Montserrat,sans-serif;font-weight:500;font-size:14px;line-height:1}
.offer p{font-family:Montserrat,sans-serif;font-size:6.5px;margin-top:3px}
.offer-green{left:71px;width:199px;background:var(--green)}
.offer-blue{left:282px;width:199px;background:var(--blue)}
.offer-red{left:490px;width:200px;background:var(--red)}

/* sidebar */
.cats{left:71px;top:490px;width:123px;height:301px;background:var(--blue);border-radius:3px;overflow:hidden}
.cats h4{background:var(--red);color:var(--white);font-weight:400;font-size:12.5px;height:28px;line-height:28px;padding-left:8px}
.cats ul{list-style:none;padding-top:4px}
.cats li{font-family:Arimo,sans-serif;font-weight:700;color:var(--white);font-size:7.5px;line-height:10px;padding:4px 4px 5px 17px;position:relative;border-bottom:1px solid rgba(255,255,255,.12)}
.cats li::before{content:"";position:absolute;left:6px;top:6px;width:6px;height:5px;border-top:2px solid var(--white);border-right:2px solid var(--white);transform:skewY(-20deg)}
.cats li.tall{padding-top:6px;padding-bottom:7px}
.cats li.tall::before{top:8px}

.social{left:74px;top:802px;width:116px;height:137px;border:1px solid var(--line);border-radius:3px;overflow:hidden;font-family:Arimo,sans-serif}
.social h4{background:var(--red);color:var(--white);font-family:"Source Sans 3",sans-serif;font-weight:400;font-size:12px;height:22px;line-height:22px;padding-left:11px}
.social .page{display:flex;gap:6px;padding:7px 0 0 10px;font-size:6px;color:#666}
.social .avatar{width:20px;height:20px;background:#8da7c4;border-radius:3px}
.social .like{display:inline-block;margin-top:3px;border:1px solid #ccd;padding:1px 4px;font-size:5.5px;color:var(--blue)}
.social .count{font-size:6px;color:#333;padding:6px 0 0 10px}
.social .faces{display:flex;gap:3px;padding:3px 0 0 3px}
.social .face{width:24px;height:24px;background:#9d8a70}
.social .names{display:flex;font-size:5.5px;padding:2px 0 0 3px}
.social .names span{width:27px;text-align:center}
.social .plug{font-size:6px;color:#667;padding:6px 0 0 8px;border-top:1px solid #eee;margin-top:5px;display:flex;gap:4px;align-items:center}
.social .plug i{width:7px;height:7px;background:var(--blue);display:inline-block}

/* products */
.featured-title{left:205px;top:492px;color:var(--blue);font-size:14.5px}
.grid{left:206px;width:490px;height:202px;border:1px solid var(--line);border-radius:4px;display:flex}
.grid-1{top:517px}
.grid-2{top:737px}
.product{flex:1;border-left:1px solid var(--line);text-align:center;position:relative}
.product:first-child{border-left:0}
.product-img{position:absolute;left:50%;top:17px;width:74px;height:76px;transform:translateX(-50%);border-radius:6px}
.product-name{position:absolute;left:0;width:100%;top:105px;font-size:9.5px;line-height:12px;color:var(--blue)}
.product-price{position:absolute;left:0;width:100%;top:130px;font-size:21px;font-weight:700;color:var(--black)}
.product-btns{position:absolute;left:0;width:100%;top:167px;display:flex;justify-content:center;gap:5px}
.product-btns .btn{font-size:6px;height:11px;line-height:11px;width:46px;font-family:Arimo,sans-serif}
.product-stars{position:absolute;left:0;width:100%;top:180px;font-size:7px}

.img-scanner{background:linear-gradient(160deg,#555,#111)}
.img-printer{background:linear-gradient(160deg,#777,#222 60%,#5a7d3a)}
.img-camera{background:linear-gradient(160deg,#6a6a6a,#1a1a1a)}
.img-remote{background:linear-gradient(180deg,#3a5a8a,#8aa0c0 60%,#cc7733)}

/* footer */
.chat-tab{left:346px;top:980px;width:68px;height:13px;background:var(--white);border-radius:2px;padding:1px}
.chat-tab span{display:block;height:11px;background:var(--green);color:var(--white);font-size:6.5px;line-height:11px;text-align:center;border-radius:1px;font-family:Arimo,sans-serif}
.footer{left:0;top:985px;width:762px;height:178px;background:var(--blue);color:var(--white);font-family:Arimo,sans-serif}
.fcol{position:absolute;top:39px}
.fcol h5{font-size:8.5px;font-weight:400;margin-bottom:10px}
.fcol ul{list-style:none}
.fcol li{font-size:6.5px;line-height:14.5px}
.fcol li::before{content:"› "}
.news p{font-size:7px;line-height:10px;width:100px}
.news .field{margin-top:10px;width:100px;height:16px;background:var(--white);color:#333;font-size:6.5px;padding:4px 6px}
.news .sub{margin-top:8px;width:100px;height:17px;background:var(--red);font-size:8px;font-weight:700;line-height:17px;text-align:center}
.post{display:flex;gap:7px;margin-bottom:11px}
.post-date{width:26px;height:27px;background:var(--white);color:var(--blue);text-align:center;border-left:3px solid var(--blue)}
.post-date b{display:block;font-size:14px;line-height:16px}
.post-date small{display:block;font-size:5px;color:#333}
.post h6{font-size:8px;color:#f7941d;font-weight:700}
.post p{font-size:7px;line-height:10px}
.post u{font-size:7px}
.map{left:577px;top:60px;width:121px;height:80px;border:2px solid #dfe8f2;border-radius:2px;background:linear-gradient(135deg,#cfdbe6,#e9e6d8 55%,#b9cde0)}

.bottombar{left:0;top:1163px;width:762px;height:37px;background:#0d0d0d;color:var(--white);font-family:Arimo,sans-serif}
.copy{position:absolute;left:62px;top:15px;font-size:6.5px}
.social-dots{position:absolute;left:401px;top:10px;display:flex;gap:4px}
.social-dots i{width:15px;height:15px;border-radius:50%;background:var(--white)}
.cards{position:absolute;left:555px;top:11px;display:flex;gap:3px}
.cards span{width:27px;height:15px;background:#e8eef5;color:#1d3f73;font-size:5px;font-weight:700;text-align:center;line-height:15px;border-radius:1px;overflow:hidden;white-space:nowrap}
</style>
</head>
<body>

<header>
  <div class="abs brand">
    <span class="brand-mark"></span>
    <span class="brand-name">Inkwell Printing</span>
  </div>
  <div class="abs call">
    <svg width="16" height="16" viewBox="0 0 16 16" aria-hidden="true"><circle cx="8" cy="8" r="7" fill="none" stroke="#111" stroke-width="1.4"/><path d="M5.5 4.5l1.5 1.5-1 1c.6 1.2 1.6 2.2 2.8 2.8l1-1 1.5 1.5-1 1.3C7.8 11.4 4.6 8.2 4.4 5.5z" fill="#111"/></svg>
    <span>Call: +123 - 555 - 0190</span>
  </div>
  <div class="abs search">
    <span>Search here...</span>
    <svg width="9" height="9" viewBox="0 0 10 10" aria-hidden="true"><circle cx="4" cy="4" r="3" fill="none" stroke="#888" stroke-width="1.3"/><path d="M6.3 6.3L9 9" stroke="#888" stroke-width="1.5"/></svg>
  </div>
</header>

<nav class="abs nav">
  <span style="left:88px">Home</span>
  <span class="active" style="left:161px">Hardware</span>
  <span style="left:239px">Licensing</span>
  <span style="left:327px">Management</span>
  <span style="left:438px">Technology Services</span>
  <span style="left:537px">Benefits</span>
  <span style="left:602px">Blog</span>
  <span style="left:666px">Contact</span>
</nav>

<section class="abs intro">
  <h1>Lorem Ipsum is simply dummy text of the printing</h1>
  <p>It is a long established fact that a reader will be distracted by the readable content</p>
</section>

<section class="abs showcase">
  <div class="show-item" style="left:36px;top:45px;width:130px">
    <div class="show-img" role="img" aria-label="Blue and white inkjet printer with paper" style="width:120px;height:110px;margin:0 auto;background:linear-gradient(160deg,#e8eef4,#2f7fd0 55%,#b8c2cc)"></div>
    <div style="margin-top:23px">Printer lorem ipsum</div>
  </div>
  <div class="show-item" style="left:415px;top:70px;width:150px">
    <div class="show-img" role="img" aria-label="Assortment of electronics accessories" style="width:140px;height:95px;margin:0 auto;background:linear-gradient(160deg,#3a4a6a,#888 50%,#c43)"></div>
    <div style="margin-top:20px">All Accessories</div>
  </div>
</section>

<article class="abs feature-card">
  <svg class="ribbon" width="72" height="72" viewBox="0 0 72 72" aria-hidden="true"><path d="M0 0H72L0 72Z" fill="#cc0e0e"/></svg>
  <div class="ribbon-text"><b>$1150</b><small>Offer10%</small><em>Off</em></div>
  <div class="show-img" role="img" aria-label="Silver flatbed scanner with blue light" style="position:absolute;left:40px;top:32px;width:135px;height:115px;background:linear-gradient(170deg,#d8d8d8,#5a5a5a 50%,#1bb6ff 62%,#c8c8c8)"></div>
  <div class="feature-title">Lorem ipsum Dolor Consectetur</div>
  <div class="feature-btns"><span class="btn btn-red">Add to Cart</span><span class="btn btn-blue">More Details</span></div>
  <div class="feature-stars stars">★★★★★</div>
</article>

<section>
  <div class="abs offer offer-green">
    <span class="offer-icon"><svg width="12" height="12" viewBox="0 0 12 12" aria-hidden="true"><rect x="1" y="4" width="10" height="7" fill="none" stroke="#fff" stroke-width="1.3"/><path d="M6 4v7M1 6.5h10" stroke="#fff" stroke-width="1.2"/></svg></span>
    <div><h3>SPECIAL OFFER</h3><p>UP TO 20% OFF ON COLLECTION</p></div>
  </div>
  <div class="abs offer offer-blue">
    <span class="offer-icon"><svg width="12" height="12" viewBox="0 0 12 12" aria-hidden="true"><rect x="2" y="1.5" width="8" height="8" rx="1.5" fill="none" stroke="#fff" stroke-width="1.3"/><path d="M2 6h8" stroke="#fff" stroke-width="1.1"/><circle cx="4" cy="10.5" r="1" fill="#fff"/><circle cx="8" cy="10.5" r="1" fill="#fff"/></svg></span>
    <div><h3>FREE SHIPPING</h3><p>UP TO 20% OFF ON COLLECTION</p></div>
  </div>
  <div class="abs offer offer-red">
    <span class="offer-icon"><svg width="12" height="12" viewBox="0 0 12 12" aria-hidden="true"><circle cx="6" cy="4" r="2.3" fill="#fff"/><path d="M1.5 11.5c.5-3 2.3-4.3 4.5-4.3s4 1.3 4.5 4.3z" fill="#fff"/></svg></span>
    <div><h3>BEST SELLER</h3><p>UP TO 20% OFF ON COLLECTION</p></div>
  </div>
</section>

<aside class="abs cats">
  <h4>Product Catogories</h4>
  <ul>
    <li>dummy text of the printing</li>
    <li>dummy text of the printing and typesetting industry.</li>
    <li>dummy text of the printing</li>
    <li>dummy text of the printing and typesetting industry.</li>
    <li class="tall">dummy text of the printing</li>
    <li class="tall">dummy text of the printing</li>
    <li class="tall">dummy text of the printing</li>
    <li class="tall">dummy text of the printing</li>
    <li class="tall">dummy text of the printing</li>
    <li class="tall">dummy text of the printing</li>
    <li class="tall" style="border-bottom:0">dummy text of the printing</li>
  </ul>
</aside>

<aside class="abs social">
  <h4>Community</h4>
  <div class="page"><span class="avatar"></span><div>Inkwell Printing<br><span class="like">Like</span></div></div>
  <div class="count">111 people like InkwellPrinting</div>
  <div class="faces">
    <span class="face" role="img" aria-label="Member photo"></span>
    <span class="face" role="img" aria-label="Member photo" style="background:#b48a5a"></span>
    <span class="face" role="img" aria-label="Member photo" style="background:#6f5a4a"></span>
    <span class="face" role="img" aria-label="Member photo" style="background:#5f7a5a"></span>
  </div>
  <div class="names"><span>Lorem</span><span>Ipsum</span><span>Doe</span><span>Stephen</span></div>
  <div class="plug"><i></i>Community social plugin</div>
</aside>

<h2 class="abs featured-title" style="font-weight:400">Our Featured Products</h2>

<section class="abs grid grid-1">
  <div class="product">
    <div class="product-img img-scanner" role="img" aria-label="Black flatbed scanner"></div>
    <div class="product-name">Lorem ipsum<br>Dolor Consectetur</div>
    <div class="product-price">$1150</div>
    <div class="product-btns"><span class="btn btn-red">Add to Cart</span><span class="btn btn-blue">More Details</span></div>
    <div class="product-stars stars">★★★★★</div>
  </div>
  <div class="product">
    <div class="product-img img-printer" role="img" aria-label="Photo printer printing a picture"></div>
    <div class="product-name">Lorem ipsum<br>Dolor Consectetur</div>
    <div class="product-price">$1050</div>
    <div class="product-btns"><span class="btn btn-red">Add to Cart</span><span class="btn btn-blue">More Details</span></div>
    <div class="product-stars stars">★★★★★</div>
  </div>
  <div class="product">
    <div class="product-img img-camera" role="img" aria-label="Digital SLR camera"></div>
    <div class="product-name">Lorem ipsum<br>Dolor Consectetur</div>
    <div class="product-price">$1450</div>
    <div class="product-btns"><span class="btn btn-red">Add to Cart</span><span class="btn btn-blue">More Details</span></div>
    <div class="product-stars stars">★★★★★</div>
  </div>
  <div class="product">
    <div class="product-img img-remote" role="img" aria-label="Handheld remote device with keyring"></div>
    <div class="product-name">Lorem ipsum<br>Dolor Consectetur</div>
    <div class="product-price">$950</div>
    <div class="product-btns"><span class="btn btn-red">Add to Cart</span><span class="btn btn-blue">More Details</span></div>
    <div class="product-stars stars">★★★★★</div>
  </div>
</section>

<section class="abs grid grid-2">
  <div class="product">
    <div class="product-img img-scanner" role="img" aria-label="Black flatbed scanner"></div>
    <div class="product-name">Lorem ipsum<br>Dolor Consectetur</div>
    <div class="product-price">$1150</div>
    <div class="product-btns"><span class="btn btn-red">Add to Cart</span><span class="btn btn-blue">More Details</span></div>
    <div class="product-stars stars">★★★★★</div>
  </div>
  <div class="product">
    <div class="product-img img-printer" role="img" aria-label="Photo printer printing a picture"></div>
    <div class="product-name">Lorem ipsum<br>Dolor Consectetur</div>
    <div class="product-price">$1050</div>
    <div class="product-btns"><span class="btn btn-red">Add to Cart</span><span class="btn btn-blue">More Details</span></div>
    <div class="product-stars stars">★★★★★</div>
  </div>
  <div class="product">
    <div class="product-img img-camera" role="img" aria-label="Digital SLR camera"></div>
    <div class="product-name">Lorem ipsum<br>Dolor Consectetur</div>
    <div class="product-price">$1450</div>
    <div class="product-btns"><span class="btn btn-red">Add to Cart</span><span class="btn btn-blue">More Details</span></div>
    <div class="product-stars stars">★★★★★</div>
  </div>
  <div class="product">
    <div class="product-img img-remote" role="img" aria-label="Handheld remote device with keyring"></div>
    <div class="product-name">Lorem ipsum<br>Dolor Consectetur</div>
    <div class="product-price">$950</div>
    <div class="product-btns"><span class="btn btn-red">Add to Cart</span><span class="btn btn-blue">More Details</span></div>
    <div class="product-stars stars">★★★★★</div>
  </div>
</section>

<footer class="abs footer">
  <div class="fcol" style="left:62px">
    <h5>ABOUT US</h5>
    <ul><li>Home</li><li>Hardware</li><li>Software</li><li>Services</li><li>Contact</li></ul>
  </div>
  <div class="fcol" style="left:135px">
    <h5>LATEST PRODUCTS</h5>
    <ul><li>Lorem Ipsum</li><li>Dummy Product</li><li>Standard lorem</li><li>Lorem Ipsum</li><li>Dummy Product</li></ul>
  </div>
  <div class="fcol news" style="left:249px">
    <h5>NEWSLETTER SIGNUP</h5>
    <p>Adipisicing elit Lorem ipsum dolor sit consectetur..</p>
    <div class="field">Enter Email</div>
    <div class="sub">Subscribde Now</div>
  </div>
  <div class="fcol" style="left:383px">
    <h5>LATEST BLOG POST</h5>
    <div class="post">
      <div class="post-date"><b>15</b><small>JULY</small></div>
      <div><h6>Consectetur adipisicing elit</h6><p>Lorem ipsum dolor sit consectetur..</p><u>Learn More</u></div>
    </div>
    <div class="post">
      <div class="post-date"><b>15</b><small>JULY</small></div>
      <div><h6>Consectetur adipisicing elit</h6><p>Lorem ipsum dolor sit consectetur..</p><u>Learn More</u></div>
    </div>
  </div>
  <div class="fcol" style="left:573px">
    <h5>CONTACT US</h5>
  </div>
  <div class="abs map" role="img" aria-label="Street map showing the store location"></div>
</footer>

<div class="abs chat-tab"><span>LIVE CHAT</span></div>

<div class="abs bottombar">
  <div class="copy">Copyright © 2013, inkwellprinting-demo.com, All Rights Reserved.</div>
  <div class="social-dots"><i></i><i></i><i></i><i></i></div>
  <div class="cards"><span>Quillpay</span><span>Torva</span><span>Amblex</span><span>Driscova</span><span>Marlocard</span></div>
</div>

</body>
</html>
```